Bref créative
Brochure for Professional Services Firm
Brightfen Partners
We need a great design for a brochure to be used as marketing collateral at tradeshows and for general marketing purposes. Our website is brightfenpartners.example to get additional information. We generally work with oilfield service companies.
Consulting
Corporate, professional.
===========Update==========
Requirement : Trifold
Our logo files.
Here is a sample presentation we currently use to market our services.
Some stock photos we have.
stock photos.
stock photo.

```html
<!DOCTYPE html>
<html lang="en">
<head>
<meta charset="utf-8">
<title>Brightfen Partners — Trifold Brochure</title>
<link href="https://fonts.googleapis.com/css2?family=Arimo:wght@400;700&display=swap" rel="stylesheet">
<style>
:root{
  --cyan:#1aa6dc;
  --ink:#3a3a3a;
  --white:#ffffff;
  --panel-dark:#5b5e61;
  --photo-top:#8a8d90;
  --photo-bottom:#4a4c4e;
  --tick:#1aa6dc;
}
*{margin:0;padding:0;box-sizing:border-box}
html,body{width:1200px;height:787px;overflow:hidden;background:var(--white)}
body{font-family:'Arimo',Arial,sans-serif;color:var(--ink)}
.brochure{position:relative;width:1200px;height:787px;display:flex}
.panel{position:relative;height:100%}
.panel-left{width:420px;padding:72px 26px 0 22px}
.panel-center{width:365px;background:linear-gradient(180deg,var(--photo-top),var(--photo-bottom));overflow:hidden}
.panel-right{width:415px;padding:72px 22px 0 32px}
.heading{color:var(--cyan);font-weight:700;font-size:34px;line-height:1;letter-spacing:.5px;text-transform:uppercase}
.body-text{font-size:14.5px;line-height:17.5px;margin-top:4px}
.num-list{list-style:none;margin-top:18px;font-size:14.5px;line-height:17.5px}
.num-list li{margin-bottom:2px}
.num{color:var(--cyan);font-size:22px;font-weight:400;margin-right:4px;vertical-align:-2px}
.side-photo{display:block;width:389px;height:120px;margin:20px 0 22px;background:linear-gradient(90deg,#2e2f31,#9b9d9f 60%,#5d5f61)}
.section-gap{margin-top:24px}
.center-photo{position:absolute;inset:0;background:linear-gradient(180deg,#7b7e81 0%,#a7a9ab 45%,#6c6f71 70%,#55585a 100%)}
.center-title{position:absolute;left:40px;top:138px;width:290px;color:var(--white);font-weight:700;font-size:36px;line-height:40px}
.brand{position:absolute;left:62px;top:642px;display:flex;align-items:center;gap:12px;color:var(--white);font-weight:700;font-size:24px;letter-spacing:2px}
.brand-mark{width:30px;height:30px;background:var(--white)}
.tick-list{list-style:none;font-size:14.5px;line-height:17.5px;margin-top:14px}
.tick-list li{position:relative;padding-left:20px}
.tick-list li svg{position:absolute;left:0;top:3px}
.tick-list .sub{margin-top:2px}
.team-name{font-weight:700}
</style>
</head>
<body>
<div class="brochure">

  <section class="panel panel-left">
    <h2 class="heading">Our Approach</h2>
    <p class="body-text">We are unique in our ability and experience in working with small and mid-market private companies:</p>
    <ul class="num-list">
      <li><span class="num">1</span>Focused on energy, oilfield, manufacturing</li>
      <li><span class="num">2</span>Several years of experience working at executive levels in small and mid–market companies gives us a valued perspective and construction service companies</li>
    </ul>
    <div class="side-photo" role="img" aria-label="Photo of an industrial drilling rig against the sky"></div>
    <ul class="num-list" style="margin-top:0">
      <li><span class="num">3</span>Ability to bridge the gap and act as a buffer between current business owners and current investors or potential purchasers</li>
      <li><span class="num">4</span>Proven history of preparing companies and successfully guiding them through a transaction</li>
    </ul>
    <h2 class="heading section-gap">Transactions</h2>
    <p class="body-text">Having a thorough understanding of our client's business increases the likelihood of a successful transaction</p>
  </section>

  <section class="panel panel-center">
    <div class="center-photo" role="img" aria-label="Photo of oilfield pipe handling equipment on a worksite"></div>
    <h1 class="center-title">We provides financial and transaction advisory services</h1>
    <div class="brand"><span class="brand-mark"></span>BRIGHTFEN PARTNERS</div>
  </section>

  <section class="panel panel-right">
    <h2 class="heading">Client Profile</h2>
    <p class="body-text">We usually work with the following types of clients:</p>
    <ul class="tick-list">
      <li><svg width="14" height="12" viewBox="0 0 14 12"><path d="M1 6l4 4 8-9" fill="none" stroke="var(--tick)" stroke-width="2.4"/></svg>Private business owners who are looking to:</li>
      <li><svg width="14" height="12" viewBox="0 0 14 12"><path d="M1 6l4 4 8-9" fill="none" stroke="var(--tick)" stroke-width="2.4"/></svg>Sell a majority position in their business</li>
      <li><svg width="14" height="12" viewBox="0 0 14 12"><path d="M1 6l4 4 8-9" fill="none" stroke="var(--tick)" stroke-width="2.4"/></svg>Select a financial partner to fund their growth or expansion plans</li>
      <li><svg width="14" height="12" viewBox="0 0 14 12"><path d="M1 6l4 4 8-9" fill="none" stroke="var(--tick)" stroke-width="2.4"/></svg>Ensure their business is scalable and capable of anticipated growth</li>
      <li><svg width="14" height="12" viewBox="0 0 14 12"><path d="M1 6l4 4 8-9" fill="none" stroke="var(--tick)" stroke-width="2.4"/></svg>Improve their accounting and reporting processes to keep pace with their operational growth</li>
      <li><svg width="14" height="12" viewBox="0 0 14 12"><path d="M1 6l4 4 8-9" fill="none" stroke="var(--tick)" stroke-width="2.4"/></svg>Private-equity or investor-owned businesses that are interested in:</li>
      <li><svg width="14" height="12" viewBox="0 0 14 12"><path d="M1 6l4 4 8-9" fill="none" stroke="var(--tick)" stroke-width="2.4"/></svg>Improving accounting and reporting functions at a porPolio company</li>
      <li><svg width="14" height="12" viewBox="0 0 14 12"><path d="M1 6l4 4 8-9" fill="none" stroke="var(--tick)" stroke-width="2.4"/></svg>Retaining an Interim-CFO or Controller at a porPolio or target company</li>
      <li><svg width="14" height="12" viewBox="0 0 14 12"><path d="M1 6l4 4 8-9" fill="none" stroke="var(--tick)" stroke-width="2.4"/></svg>Assistance with due-diligence and data room preparations</li>
    </ul>
    <h2 class="heading section-gap">Team</h2>
    <p class="body-text">We are a small firm by design. It allows us to be selective and limit the number of our engagements to provide the personalized service our clients expect.<br>
      <span class="team-name">Grant Holloway, CPA</span> –<br>Managing Partner<br>
      <span class="team-name">Owen Maresca, CPA</span> –<br>Senior Associate</p>
  </section>

</div>
</body>
</html>
```